Business card design needed

My company does everything from wiring up your exisiting entertainment system, to installing a complete new system for you. We can mount your plasma on the wall, install an aerial point for you, setup some surround sound in your outdoor area or install a new cinema room in your house. Any Audio or Visual requirements you may have we can provide these for you. If you want to have a party to remember at your place or just some chilled sounds by the pool, we can give you just the right size system.

Industry/Entity Type

Entertainment

Contact Information for Business Card

The Tune Crew
Colin Pemberton
e| colin@thetunecrew.com.au
w| www.thetunecrew.com.au
m| 0412 576 208

Requirements
Must have
• The logo that i have uploaded is just a starter...something similar to this but not exact or any new suggestions you have would be great too. Colour choice we are pretty easy on we did think Red and Yellow but happy to take advice, something that stands out from the rest i guess.

```html
<!DOCTYPE html>
<html lang="en">
<head>
<meta charset="utf-8">
<title>The Tune Crew – Business Card</title>
<link rel="stylesheet" href="https://fonts.googleapis.com/css2?family=PT+Sans+Narrow:wght@400;700&display=swap">
<style>
  :root {
    --page: #ffffff;
    --sun: #fedb4d;
    --ink: #000000;
    --disc: #080904;
  }
  html, body {
    margin: 0;
    padding: 0;
    width: 1000px;
    height: 1200px;
    overflow: hidden;
    background: var(--page);
  }
  .canvas {
    position: relative;
    width: 1000px;
    height: 1200px;
    font-family: "PT Sans Narrow", "Arial Narrow", sans-serif;
  }
  .card {
    position: absolute;
    left: 253px;
    top: 207px;
    width: 508px;
    height: 878px;
  }
  .card-top {
    position: absolute;
    left: 0;
    top: 0;
    width: 508px;
    height: 564px;
    background: var(--sun);
  }
  .brand-disc {
    position: absolute;
    left: 68px;
    top: 50px;
    width: 374px;
    height: 374px;
    border-radius: 50%;
    background: var(--disc);
    display: flex;
    align-items: center;
    justify-content: center;
  }
  .brand-disc-name {
    color: var(--sun);
    font-weight: 700;
    font-size: 54px;
    letter-spacing: 0.5px;
  }
  .company-name {
    position: absolute;
    left: 0;
    top: 482px;
    width: 508px;
    margin: 0;
    text-align: center;
    font-size: 40px;
    font-weight: 700;
    line-height: 50px;
    color: var(--ink);
  }
  .card-bottom {
    position: absolute;
    left: 0;
    top: 564px;
    width: 508px;
    height: 314px;
    background: var(--ink);
    color: var(--sun);
  }
  .person-name {
    position: absolute;
    left: 0;
    top: 42px;
    width: 508px;
    margin: 0;
    text-align: center;
    font-size: 34px;
    font-weight: 700;
    line-height: 44px;
  }
  .contact-list {
    position: absolute;
    left: 0;
    top: 120px;
    margin: 0;
    padding: 0;
    list-style: none;
    font-size: 33px;
    line-height: 55px;
  }
  .contact-item {
    display: flex;
    align-items: center;
    white-space: nowrap;
  }
  .contact-label {
    display: inline-block;
    width: 101px;
    text-align: right;
  }
  .contact-rule {
    display: inline-block;
    width: 3px;
    height: 36px;
    margin: 0 9px 0 6px;
    background: var(--sun);
  }
</style>
</head>
<body>
<div class="canvas">
  <div class="card">
    <div class="card-top">
      <div class="brand-disc">
        <span class="brand-disc-name">The Tune Crew</span>
      </div>
      <h1 class="company-name">The Tune Crew</h1>
    </div>
    <div class="card-bottom">
      <h2 class="person-name">Colin Pemberton</h2>
      <ul class="contact-list">
        <li class="contact-item"><span class="contact-label">e</span><span class="contact-rule"></span><span>colin@thetunecrew.com.au</span></li>
        <li class="contact-item"><span class="contact-label">w</span><span class="contact-rule"></span><span>www.thetunecrew.com.au</span></li>
        <li class="contact-item"><span class="contact-label">m</span><span class="contact-rule"></span><span>0412 576 208</span></li>
      </ul>
    </div>
  </div>
</div>
</body>
</html>
```